Business card for Industrial Automation Company.

The company is called Process and Signal Dynamics. We are a systems integration company in South Africa specializing in PLC and SCADA programming, systems integration and industrial automation. Attached find logo and cover letter of the company for a feel of the general look. The website is still under development, so you will have to use your own ideas.

Please blend the colors on the business card as per the logo colors. Must be clean, professional look. Please submit a creative professional design. If a background color is used please do not use dark colored backgrounds.

Target Market(s)

Mining

Industry/Entity Type

Engineering Consultant

Contact Information for Business Card

Gerrit van Dyk (NDip Instrumentation; BEng)
Managing Partner / Control Engineer

Postal Address
PO Box 2867
Vredenburg
7380

Physical Address:
Kloofhoek Street 27
Vredenburg
7380

Tel: +22 548 6170
Cell: +27 82 953 4086
Mail: gerritv@psd-zx.com
Web: www.psd-zx.com

Font styles to use
Sans Serif

Colors

Designer to choose colors to be used in the design.

Requirements
Must have
• Backside of the card must also contain the following:
• Services
• *Industrial Automation
• *Control System design and configuration
• *Systems Integration
• *Equipment Supply
• Industries
• *Mining
• *Factory
• *Oil and Gas
Nice to have
• Colors must blend in with colors of logo. Not too much color and no dark backgrounds.
Should not have
• dark / black background. Preferably white / light background if any.

```html
<!DOCTYPE html>
<html lang="en">
<head>
<meta charset="utf-8">
<title>Process and Signal Dynamics – Business Cards</title>
<link rel="stylesheet" href="https://fonts.googleapis.com/css2?family=Open+Sans:wght@300;400;600;700;800&display=swap">
<style>
  :root {
    --navy: #1d3f80;
    --accent: #e4e64c;
    --grey: #6b6e73;
    --paper: #ffffff;
    --backdrop: #eceef1;
  }
  * { box-sizing: border-box; margin: 0; padding: 0; }
  html, body {
    width: 1200px; height: 900px; overflow: hidden;
    background: var(--backdrop);
    font-family: "Open Sans", Arial, sans-serif;
  }
  .stage { position: relative; width: 1200px; height: 900px; }
  .card {
    position: absolute; left: 280px; width: 640px; height: 380px;
    background: var(--paper); border-radius: 28px; overflow: hidden;
    box-shadow: 0 10px 28px rgba(20, 40, 80, 0.18);
    color: var(--navy);
  }
  .card--services { top: 50px; }
  .card--contact { top: 470px; }

  /* brand block */
  .brand { position: absolute; left: 40px; top: 26px; right: 40px; height: 116px; }
  .brand__dot {
    position: absolute; left: 0; top: 10px; width: 78px; height: 78px;
    border-radius: 50%; background: var(--navy);
  }
  .brand__divider {
    position: absolute; left: 100px; top: 4px; width: 2px; height: 90px; background: var(--accent);
  }
  .brand__name {
    position: absolute; left: 116px; top: 0;
    font-weight: 800; font-size: 28px; line-height: 31px; color: var(--navy);
  }
  .brand__tagline {
    position: absolute; left: 116px; top: 96px; white-space: nowrap;
    font-weight: 300; font-size: 15px; letter-spacing: 2px; color: var(--grey);
  }
  .rule { position: absolute; left: 0; right: 0; top: 150px; height: 5px; background: var(--navy); }

  /* services side */
  .services { position: absolute; left: 0; right: 0; top: 166px; text-align: center; }
  .services__heading { font-weight: 800; font-size: 19px; line-height: 26px; color: var(--navy); }
  .services__list { list-style: none; margin-top: 4px; }
  .services__list li { font-weight: 400; font-size: 17px; line-height: 23px; color: var(--navy); }

  /* contact side */
  .person { position: absolute; left: 40px; top: 168px; }
  .person__name { font-weight: 700; font-size: 19px; line-height: 26px; }
  .person__role { font-weight: 400; font-size: 16px; line-height: 24px; margin-left: 70px; }
  .phones {
    position: absolute; right: 36px; top: 232px;
    font-size: 12.5px; line-height: 20px; color: var(--navy);
  }
  .addresses {
    position: absolute; left: 40px; top: 244px;
    font-size: 12.5px; line-height: 15px; color: var(--navy);
  }
  .addresses p + p { margin-top: 8px; }

  /* footer band */
  .band { position: absolute; left: 0; bottom: 0; width: 640px; height: 90px; }
  .band path { fill: var(--navy); }
  .band__email { position: absolute; left: 60px; bottom: 10px; font-size: 17px; color: var(--paper); }
  .band__web { position: absolute; right: 60px; bottom: 40px; font-size: 16px; color: var(--paper); }
</style>
</head>
<body>
<main class="stage">

  <section class="card card--services" aria-label="Card back: services">
    <div class="brand">
      <span class="brand__dot"></span>
      <span class="brand__divider"></span>
      <div class="brand__name">Process<br>and Signal<br>Dynamics</div>
      <div class="brand__tagline">Engineering dependable process control!</div>
    </div>
    <div class="rule"></div>
    <div class="services">
      <h2 class="services__heading">Services for Mining, Factory, Oil and Gas</h2>
      <ul class="services__list">
        <li>Industrial Automation</li>
        <li>Control System Design and Configuration</li>
        <li>Systems Integration</li>
        <li>Equipment Supply</li>
      </ul>
    </div>
    <svg class="band" viewBox="0 0 640 90" aria-hidden="true">
      <path d="M0,46 L330,46 C380,46 380,8 430,8 L640,8 L640,90 L0,90 Z"/>
    </svg>
    <span class="band__email">gerritv@psd-zx.com</span>
    <span class="band__web">www.psd-zx.com</span>
  </section>

  <section class="card card--contact" aria-label="Card front: contact details">
    <div class="brand">
      <span class="brand__dot"></span>
      <span class="brand__divider"></span>
      <div class="brand__name">Process<br>and Signal<br>Dynamics</div>
      <div class="brand__tagline">Engineering dependable process control!</div>
    </div>
    <div class="rule"></div>
    <div class="person">
      <p class="person__name">Gerrit van Dyk (NDip Instrumentation; BEng)</p>
      <p class="person__role">Managing Partner / Control Engineer</p>
    </div>
    <div class="phones">
      <p>Tel: +22 548 6170</p>
      <p>Cell: +27 82 953 4086</p>
    </div>
    <div class="addresses">
      <p>Postal Address<br>PO Box 2867, Duinefontein 7412</p>
      <p>Physical Address<br>Kloofhoek Street 27, Duinefontein 7412</p>
    </div>
    <svg class="band" viewBox="0 0 640 90" aria-hidden="true">
      <path d="M0,46 L330,46 C380,46 380,8 430,8 L640,8 L640,90 L0,90 Z"/>
    </svg>
    <span class="band__email">gerritv@psd-zx.com</span>
    <span class="band__web">www.psd-zx.com</span>
  </section>

</main>
</body>
</html>
```